Aufgabenstellung
!!!FÜR UNSRE LUMIRA WERBEPLUS KAMPAGNE!!!
...benötigt werden folgende Formate, wobei in diesem Wettbewerb nur eines dieser Formate gewählt werden soll. Der Gewinner sollte dann die restlichen Formate nachreichen. Es handelt sich um animierte GIFs
Leaderboard 728 x 90
Inline Rectangle 300 x 250
Wide Sycreaper 160 x 600
Banner 468 x 60
Large Rectangle 336 x 280
Small Square 200 x 200
Square 250 x 250
Für eine Landingpage benötigen wir entsprechende Banner. Es handelt sich um einen geschlossenen Fonds namens „TRV 12 Wellenreiter“. Der Vorteil dieses Fonds liegt darin, dass es nicht ein einziger Fonds ist, sondern ein Dachfonds, der viele andere Fonds am Zweitmarkt einkauft. Zweitmarktfonds sind geschlossene Fonds, die bereits länger laufen und sich im Gegensatz zu Neuemissionen (neue Fonds) bereits bewährt haben. Meist wurden die Kredite für die Finanzierung der Immobilie deutlich getilgt und es bestehen eher geringe Restschulden.
Das Risiko für den Anleger ist somit bei einem Zweitmarktfonds deutlich geringer und besser einzuschätzen. Hinzu kommt, dass der TRV 12 Wellenreiter auch noch auf viele verschiedene Zweitmarktfonds streut. Es handelt sich immer um Schiffsfonds. Insgesamt ist also zu sagen:
Der Fonds streut auf viele Schiffe, die sich bereits bewährt haben. Das Wording kann lauten:
"Lieber den Seemann im Boot als die Katze im Sack!"
Was die Bilder betrifft, möchte ich die Wahl dem Designer überlassen. Ich bitte Sie hier, die typischen Bilddatenbanken zu nutzen und einen geeigneten Vorschlag zu machen. Das entsprechende Bild werden wir dann auch in unsere Landingpage einbauen. Was soll das Bild transortieren:
Erfahrung, breite Risikostreuung, Schlauheit, Intelligenz.
Die Rendite von 7,7 % p.a. sollte mit eingebaut werden. Bitte berücksichtigen Sie, dass man mit einem Banner maximal 3 Sekunden Zeit hat, die Botschaft rüber ..

```html
<!DOCTYPE html>
<html lang="de">
<head>
<meta charset="utf-8">
<title>TRV 12 Wellenreiter – Leaderboard</title>
<link href="https://fonts.googleapis.com/css2?family=Roboto+Condensed:wght@400;700&display=swap" rel="stylesheet">
<style>
  :root {
    --brand-red: #a8192a;
    --headline-red: #b8232f;
    --ink: #3a3a3a;
    --white: #ffffff;
    --sky: #dfe3e6;
    --harbour: #8d9499;
    --hull: #b3262c;
  }
  * { margin: 0; padding: 0; box-sizing: border-box; }
  html, body { width: 1200px; height: 148px; overflow: hidden; background: var(--white); }
  .banner {
    position: relative;
    width: 1200px;
    height: 148px;
    overflow: hidden;
    background: var(--white);
    font-family: "Roboto Condensed", "Arial Narrow", sans-serif;
  }
  .harbour-photo {
    position: absolute;
    left: 220px; top: 0;
    width: 880px; height: 148px;
    background:
      linear-gradient(90deg, var(--white) 0%, rgba(255,255,255,0) 12%, rgba(255,255,255,0) 88%, var(--white) 100%),
      linear-gradient(180deg, var(--sky) 0%, var(--sky) 30%, rgba(223,227,230,0) 55%),
      linear-gradient(90deg, var(--harbour) 0%, #7f8a90 35%, #9b5a52 60%, var(--hull) 80%, #c9c9c9 100%);
  }
  .issuer {
    position: absolute;
    left: 8px; top: 34px;
    width: 214px;
  }
  .issuer-name {
    font-size: 22px;
    font-weight: 400;
    line-height: 26px;
    color: var(--ink);
    white-space: nowrap;
    padding-left: 4px;
  }
  .yield-badge {
    margin-top: 18px;
    height: 43px;
    background: var(--brand-red);
    color: var(--white);
    font-size: 30px;
    font-weight: 400;
    line-height: 43px;
    text-align: center;
  }
  .headline {
    position: absolute;
    left: 340px; top: 10px;
    color: var(--headline-red);
    font-weight: 700;
    font-size: 35px;
    line-height: 41px;
    white-space: nowrap;
  }
  .cta {
    position: absolute;
    left: 565px; top: 104px;
    display: flex; align-items: center;
    text-decoration: none;
  }
  .cta-label {
    background: var(--brand-red);
    color: var(--white);
    font-size: 16px;
    font-weight: 700;
    padding: 3px 12px;
    border: 1px solid var(--white);
  }
  .cta-cursor { margin-left: -6px; margin-top: 10px; }
  .partner {
    position: absolute;
    right: 0; top: 0;
    width: 118px; height: 148px;
    background: var(--white);
    display: flex; align-items: center; justify-content: center;
  }
  .partner-name {
    color: var(--ink);
    font-weight: 400;
    font-size: 26px;
  }
</style>
</head>
<body>
  <div class="banner">
    <div class="harbour-photo" role="img" aria-label="Containerschiff im Hafen vor grauem Himmel"></div>

    <div class="issuer">
      <p class="issuer-name">TRV Seekapital AG</p>
      <p class="yield-badge">7.7 % Rendite</p>
    </div>

    <h1 class="headline">Der einzige Musterschüler<br>in der Schiffsklasse.</h1>

    <a class="cta" href="#">
      <span class="cta-label">zum Fonds</span>
      <svg class="cta-cursor" width="26" height="30" viewBox="0 0 26 30" aria-hidden="true">
        <path d="M8 2v15l-3-3c-2-2-4 0-3 2l6 9c1 2 3 3 5 3h5c3 0 5-3 5-6v-7c0-2-3-2-3 0v-2c0-2-3-2-3 0v-1c0-2-3-2-3 0V2c0-2-4-2-4 0z" fill="#fff" stroke="#222" stroke-width="1.4"/>
      </svg>
    </a>

    <div class="partner">
      <span class="partner-name">kolibri</span>
    </div>
  </div>
</body>
</html>
```